Flyer/Poster design required for volunteer activities

We need a STRIKING A4 Poster/Flyer advertising our conservation volunteer program activities which are currently happening in the area. This poster is to advertise the program once people have arrived on the island or to locals. The program covers 5 months, May-September 2019 and is focused on conservation. I have attached the following:
- a flyer which was previously created (Tidewatch Habitat Helpers 2019 sm)to advertise the program - would prefer it has a similar striking resemblance, but not essential
- A mock up document 'TWHH On Island Poster_2019_v2' with text -Logos-Images

Target Market(s)

Everyone interested in Environmental Adventure/Hiking/Citizen Science

Industry/Entity Type

Tourism

Font styles to use
Sans Serif

Requirements
Must have
• -A travel conservation focus
• -Must use 'LHI-Background Image' as the background to the design
• -The info of where to get more information and the social media details must be prominent

```html
<!DOCTYPE html>
<html lang="en">
<head>
<meta charset="utf-8">
<title>Tidewatch Habitat Helpers – On Island Poster 2019</title>
<link href="https://fonts.googleapis.com/css2?family=Jost:wght@400;500;600;700&display=swap" rel="stylesheet">
<style>
  :root{
    --yellow:#ffe600;
    --navy:#1b2c64;
    --white:#ffffff;
    --ink:#1c1c1c;
    --page:#c9c9c9;
    --sky:#8fb0d0;
    --cloud:#e4e8ee;
    --sea:#4f93b3;
    --lagoon:#63b3c4;
    --hill:#4d6b3f;
    --forest:#2d3a24;
    --forest-deep:#1a1e16;
  }
  *{box-sizing:border-box;margin:0;padding:0}
  html,body{width:1200px;height:1200px;overflow:hidden;background:var(--page)}
  body{position:relative;font-family:"Jost",sans-serif}

  .poster{
    position:absolute;left:210px;top:48px;width:975px;height:1380px;
    transform:scale(0.8);transform-origin:top left;overflow:hidden;
    box-shadow:0 10px 30px rgba(0,0,0,.35);
  }
  .poster-photo{
    position:absolute;inset:0;
    background:
      radial-gradient(ellipse 260px 60px at 700px 110px,rgba(255,255,255,.55),transparent 70%),
      radial-gradient(ellipse 300px 50px at 300px 70px,rgba(255,255,255,.45),transparent 70%),
      radial-gradient(ellipse 420px 120px at 520px 300px,rgba(120,190,200,.55),transparent 70%),
      radial-gradient(ellipse 240px 260px at 880px 420px,rgba(70,100,50,.85),transparent 70%),
      radial-gradient(ellipse 300px 500px at 820px 900px,rgba(60,80,45,.55),transparent 70%),
      radial-gradient(ellipse 300px 400px at 150px 850px,rgba(55,70,40,.5),transparent 70%),
      linear-gradient(180deg,var(--sky) 0%,var(--cloud) 10%,#a9c2d6 15%,var(--hill) 17%,#5c8a8f 20%,var(--sea) 23%,var(--lagoon) 28%,#6e9da5 33%,#546b4c 38%,var(--forest) 50%,var(--forest-deep) 78%,#141612 100%);
  }
  .swoosh{position:absolute;left:0;top:0;width:975px;height:700px}

  .brand{position:absolute;left:38px;top:80px;display:flex;align-items:center;gap:14px}
  .brand-dot{width:80px;height:80px;border-radius:50%;background:var(--white)}
  .brand-name{font-weight:600;font-size:28px;color:var(--white);line-height:1.1;width:230px;text-shadow:1px 2px 3px rgba(0,0,0,.45)}

  .kicker{position:absolute;left:0;top:258px;height:49px;background:var(--yellow);
    color:var(--navy);font-weight:500;font-size:40px;line-height:49px;padding:0 18px 0 40px;white-space:nowrap}
  .headline{position:absolute;left:40px;top:318px;color:var(--white);font-weight:600;font-size:54px;letter-spacing:0.5px;white-space:nowrap;text-shadow:1px 2px 4px rgba(0,0,0,.35)}

  .inset-photo{position:absolute;left:42px;top:398px;width:204px;height:204px;border-radius:50%;
    border:6px solid var(--yellow);
    background:
      radial-gradient(ellipse 60px 40px at 130px 45px,rgba(90,110,90,.9),transparent 75%),
      radial-gradient(ellipse 70px 50px at 40px 150px,rgba(140,150,90,.85),transparent 75%),
      linear-gradient(180deg,#c9d9e6 0%,#a9c6dc 14%,#5b7a62 20%,#2fa3c7 36%,#46b9cf 55%,#2a7fae 75%,#1f5f8f 100%)}

  .tagline{position:absolute;left:272px;top:446px;color:var(--yellow);font-weight:700;font-size:38px;white-space:nowrap;
    text-shadow:1px 2px 3px rgba(0,0,0,.6)}
  .pillars{position:absolute;left:282px;top:490px;color:var(--white);font-weight:600;font-size:26px;white-space:nowrap;
    text-shadow:1px 2px 3px rgba(0,0,0,.6)}

  .intro{position:absolute;left:42px;top:645px;width:893px}
  .intro-lead{color:var(--white);font-weight:600;font-size:32px;line-height:40px}
  .intro-title{color:var(--yellow);font-weight:700;font-size:40px;line-height:48px;margin-top:4px;white-space:nowrap}
  .intro-sub{color:var(--yellow);font-weight:400;font-size:23px;line-height:28px;margin-top:8px;text-align:justify}
  .intro-body{color:var(--white);font-size:19px;line-height:24px;text-align:justify;margin-top:14px}
  .intro-body + .intro-body{margin-top:10px}

  .quote{position:absolute;left:40px;top:1050px;width:893px}
  .quote-mark{position:absolute;color:var(--white);font-weight:700;font-size:40px;line-height:1}
  .quote-mark.open{left:0;top:0}
  .quote-mark.close{right:0;top:66px}
  .quote-line1{margin-left:45px;color:var(--yellow);font-size:32px;line-height:40px}
  .quote-line2{margin-left:45px;color:var(--white);font-weight:700;font-size:32px;line-height:40px}
  .quote-by{text-align:right;color:var(--white);font-size:24px;margin-top:14px}

  .contact-bar{position:absolute;left:0;top:1215px;width:975px;height:130px;background:var(--yellow);display:flex;align-items:center}
  .contact{flex:1;height:100px;display:flex;flex-direction:column;align-items:center;justify-content:center;gap:16px}
  .contact + .contact{border-left:2px solid var(--ink)}
  .contact-icon{width:40px;height:40px}
  .contact-text{font-weight:700;font-size:21px;color:var(--ink);white-space:nowrap}
  .contact-dot{width:36px;height:36px;border:4px solid var(--ink);border-radius:50%}
</style>
</head>
<body>
<div class="poster">
  <div class="poster-photo" role="img" aria-label="Hiker with backpack on a ridge overlooking the island lagoon, beaches and ocean under a cloudy sky, with palm fronds in the lower foreground"></div>

  <svg class="swoosh" viewBox="0 0 975 700" aria-hidden="true">
    <path d="M0,700 L0,505 C140,470 260,555 480,625 C660,675 860,560 975,320 L975,700 Z" fill="rgba(20,24,18,.4)"/>
    <path d="M0,505 C140,470 260,555 480,625 C660,675 860,560 975,320" fill="none" stroke="var(--yellow)" stroke-width="14"/>
  </svg>

  <div class="brand">
    <div class="brand-dot"></div>
    <div class="brand-name">Tidewatch Habitat Helpers</div>
  </div>

  <div class="kicker">MAKE A DIFFERENCE</div>
  <div class="headline">LORD HOWE ISLAND</div>

  <div class="inset-photo" role="img" aria-label="Aerial view of the island lagoon, reef and mountains"></div>

  <div class="tagline">PROTECTING PARADISE 2019</div>
  <div class="pillars">Conservation | Nature | Citizen Science</div>

  <section class="intro">
    <p class="intro-lead">JOIN OUR</p>
    <h1 class="intro-title">TIDEWATCH HABITAT HELPERS PROGRAM</h1>
    <p class="intro-sub">IN 2019 AND BE INVOLVED IN A WORLD CLASS, AWARD WINNING HOLISTIC CONSERVATION EFFORT – PROTECTING PARADISE</p>
    <p class="intro-body">Lord Howe Island and its surrounding marine park are located 600km off the New South Wales coast and are renowned for their spectacular scenery. An important breeding ground for colonies of seabirds, the rich biodiversity of Lord Howe Island includes many endangered and critically endangered species found nowhere else in the world.</p>
    <p class="intro-body">The Tidewatch Habitat Helpers program believe in protecting Lord Howe Island’s unique biodiversity while showcasing world class conservation in action. We are dedicated to empowering like-minded people to make a difference through robust citizen science, inspiring educational experiences, and tangible local conservation.</p>
  </section>

  <blockquote class="quote">
    <span class="quote-mark open">“</span>
    <p class="quote-line1">LORD HOWE ISLAND IS</p>
    <p class="quote-line2">SO EXTRAORDINARY IT IS ALMOST UNBELIEVABLE</p>
    <span class="quote-mark close">”</span>
    <p class="quote-by">Dr Marion Kestrel</p>
  </blockquote>

  <footer class="contact-bar">
    <div class="contact">
      <svg class="contact-icon" viewBox="0 0 40 40" aria-hidden="true" fill="none" stroke="var(--ink)" stroke-width="2.5">
        <circle cx="20" cy="20" r="17"/>
        <ellipse cx="20" cy="20" rx="8" ry="17"/>
        <line x1="3" y1="20" x2="37" y2="20"/>
        <path d="M6,11 H34 M6,29 H34"/>
      </svg>
      <span class="contact-text">www.tidewatchisle.info</span>
    </div>
    <div class="contact">
      <div class="contact-dot"></div>
      <span class="contact-text">www.friendsbook.net/twhh</span>
    </div>
    <div class="contact">
      <div class="contact-dot"></div>
      <span class="contact-text">picturegram @twhh</span>
    </div>
  </footer>
</div>
</body>
</html>
```